Need a business card for my new home staging and redesign business. Business name: Quillamore Interiors. Subtitle: Thoughtful Home Styling and Staging

Target Market(s)

Realtors, home sellers

Industry/Entity Type

Real Estate

Contact Information for Business Card

I don't have a website address yet, or a business Facebook account, but would like to include those. Do not have a logo or any graphics

Font styles to use
Sans Serif

Colors

Designer to choose colors to be used in the design.

Requirements
Must have
• Placeholders for contact details, e.g. Phone, email, web address, etc.
Nice to have
• Sophisticated but somewhat whimsical feel. Perhaps a stylized star (or magic wand?) over the "I" in interiors to convey inspiration.
Should not have
• Nothing too cutesy, including cartoon wizards.

```html
<!DOCTYPE html>
<html lang="en">
<head>
<meta charset="utf-8">
<title>Quillamore Interiors – Business Card</title>
<link rel="stylesheet" href="https://fonts.googleapis.com/css2?family=Lato:wght@400;700&display=swap">
<style>
  :root {
    --navy: #0f4574;
    --green: #8dc21f;
    --white: #ffffff;
    --backdrop: #e9e7e4;
    --rule: #6b8cab;
  }
  * { margin: 0; padding: 0; box-sizing: border-box; }
  html, body {
    width: 1200px; height: 900px; overflow: hidden;
    background: var(--backdrop);
    font-family: "Lato", Arial, sans-serif;
  }
  .canvas { position: relative; width: 1200px; height: 900px; }

  .card { position: absolute; overflow: hidden; }

  /* Contact side */
  .card-contact {
    left: 178px; top: 73px; width: 588px; height: 366px;
    background: var(--navy); color: var(--white);
  }
  .accent-panel { position: absolute; left: 0; top: 0; }
  .contact-block {
    position: absolute; right: 36px; top: 140px; text-align: right;
  }
  .person-name { font-weight: 700; font-size: 21px; letter-spacing: 0.5px; line-height: 1.2; }
  .person-role { font-size: 17px; line-height: 1.3; }
  .contact-list { list-style: none; margin-top: 13px; font-size: 16px; line-height: 22px; }
  .contact-list li { display: flex; justify-content: flex-end; align-items: center; gap: 4px; }
  .contact-icon { width: 13px; height: 13px; fill: var(--white); }
  .social-row {
    position: absolute; right: 36px; top: 290px;
    display: flex; align-items: center; gap: 8px;
  }
  .social-rule { width: 170px; height: 1px; background: var(--rule); margin-right: 4px; }
  .social-dot { width: 26px; height: 26px; border-radius: 50%; background: var(--white); }

  /* Brand side */
  .card-brand {
    left: 388px; top: 505px; width: 566px; height: 352px;
    background: var(--white);
  }
  .brand-mark {
    position: absolute; left: 0; right: 0; top: 128px;
    display: flex; flex-direction: column; align-items: center;
    color: var(--navy); font-weight: 400;
  }
  .brand-dot { width: 22px; height: 22px; border-radius: 50%; background: var(--green); margin-bottom: 48px; }
  .brand-name { font-size: 35px; letter-spacing: 1px; line-height: 1.1; }
  .brand-sub { font-size: 21px; letter-spacing: 14px; margin-right: -14px; line-height: 1.4; }
  .tagline-band {
    position: absolute; left: 0; bottom: 0; width: 100%; height: 55px;
    background: var(--navy); color: var(--white);
    display: flex; align-items: center; justify-content: center;
    font-weight: 700; font-size: 16px; letter-spacing: 0.3px;
  }
</style>
</head>
<body>
<main class="canvas">
  <section class="card card-contact">
    <svg class="accent-panel" width="588" height="366" viewBox="0 0 588 366" aria-hidden="true">
      <polygon points="0,0 170,0 0,366" fill="var(--green)"/>
    </svg>
    <div class="contact-block">
      <p class="person-name">MARCUS ELLERY</p>
      <p class="person-role">Managing Director</p>
      <ul class="contact-list">
        <li>444 555 0192
          <svg class="contact-icon" viewBox="0 0 16 16"><path d="M3 2h3l1.5 3.5-2 1.2a9 9 0 0 0 3.8 3.8l1.2-2L14 10v3a1 1 0 0 1-1 1A12 12 0 0 1 2 3a1 1 0 0 1 1-1z"/></svg>
        </li>
        <li>hello@quillamore.com
          <svg class="contact-icon" viewBox="0 0 16 16"><path d="M1 3h14v10H1z M2 4l6 5 6-5" fill="var(--white)" stroke="var(--navy)" stroke-width="1.2"/></svg>
        </li>
        <li>www.quillamore.com
          <svg class="contact-icon" viewBox="0 0 16 16"><circle cx="8" cy="8" r="7"/><path d="M4 5c2 0 3 1 2 3s1 3 0 5M10 2c0 2 2 2 3 3" stroke="var(--navy)" stroke-width="1.3" fill="none"/></svg>
        </li>
      </ul>
    </div>
    <div class="social-row">
      <span class="social-rule"></span>
      <span class="social-dot"></span>
      <span class="social-dot"></span>
    </div>
  </section>

  <section class="card card-brand">
    <div class="brand-mark">
      <span class="brand-dot"></span>
      <span class="brand-name">QUILLAMORE</span>
      <span class="brand-sub">INTERIORS</span>
    </div>
    <div class="tagline-band">THOUGHTFUL HOME STYLING AND STAGING</div>
  </section>
</main>
</body>
</html>
```